WP website design for Brevin

We need a wordpress design for an auction company. The winning design will incorporate a professional color scheme with company logo in a clean, image driven layout. The design needs to consider that this will be developed on a responsive theme. Colors are those that will highlight the logo.

Industry/Entity Type

It Company

Font styles to use
Serif
Sans Serif

Colors

Designer to choose colors to be used in the design.

Requirements
Must have
• Navigation: 1) Home 2) Auctions 3) Services 4) Real Estate 5 ) Previous Auctions 6) About Us 7) Contact Us

Sites referenced that client likes: https://www.pledgora.example/ and http://www.quillmoorbids.example/ as examples of image rich sites. There will be large slideshow element and 4 calls to action (with any stock images suitable) 1) Real Estate 2) Auctions 3) Liquidations 4) Appraisals

Content will also include text (below) and auctions as seen at http://www.quillmoorbids.example/ below the slideshow or as in the attached image.

Footer will have contact info, social icons (FB, Twitter, YT, RSS) and news posts widget

Colors will be that of the logo and any others to highlight/compliment the design.

Nice to have
• Use of dropdown menu styling

```html
<!DOCTYPE html>
<html lang="en">
<head>
<meta charset="utf-8">
<title>Brevin Auctions</title>
<link rel="stylesheet" href="https://fonts.googleapis.com/css2?family=Open+Sans:wght@400;600;700&family=Tinos:wght@400&display=swap">
<style>
:root{
  --navy:#14226b;
  --navy-dark:#0f1a52;
  --navy-row:#1f3278;
  --red:#e0261f;
  --orange:#f04a12;
  --ink:#1b1b1b;
  --grey-text:#666;
  --panel:#f4f4f4;
  --rule:#dcdcdc;
  --white:#fff;
}
*{margin:0;padding:0;box-sizing:border-box}
html,body{width:905px;height:1200px;overflow:hidden}
body{position:relative;background:var(--white);font-family:"Open Sans",Arial,sans-serif;color:var(--ink)}
.abs{position:absolute}

/* header */
.site-header{left:0;top:0;width:905px;height:107px;background:linear-gradient(#fff,#e6e6e6)}
.brand{display:flex;align-items:center;gap:7px;font-weight:700;color:var(--navy);font-size:17px;letter-spacing:.5px}
.brand-mark{width:14px;height:14px;background:var(--navy)}
.header-brand{left:98px;top:40px}
.contact-line{left:607px;top:22px;font-size:13px;color:#333}
.contact-line span{border-left:1px solid #333;margin-left:6px;padding-left:6px}
.search{left:610px;top:64px;width:106px;height:19px;border:1px solid #aaa;border-radius:3px;background:#fff;font-size:7px;font-style:italic;color:#777;padding:4px 7px}
.search-btn{left:696px;top:64px;width:20px;height:19px;background:var(--navy);border-radius:0 3px 3px 0}
.lang{left:747px;top:65px;display:flex;align-items:center;gap:6px;font-size:11px;color:#333}
.flag{width:22px;height:14px;background:linear-gradient(#2a3f8f,#c8323a 50%,#2a3f8f)}

/* nav */
.main-nav{left:0;top:107px;width:905px;height:40px;background:#fff}
.main-nav ul{list-style:none;display:flex;position:absolute;top:14px;left:192px;font-size:11px;font-weight:700;color:var(--navy)}
.main-nav li{margin-right:25px}
.main-nav li.current{outline:2px solid var(--red);outline-offset:4px;padding:0 1px}
.dropdown{left:310px;top:145px;width:57px;background:#2b2b2b;font-size:7px;color:#fff;padding:2px 3px}
.dropdown div{padding:2px 0;border-bottom:1px solid #555}

/* hero */
.hero{left:0;top:147px;width:905px;height:326px;background:linear-gradient(135deg,#8d8f86,#b9b3a7 40%,#6d6459 75%,#3b3631)}
.hero-caption{left:97px;top:249px;width:236px;height:156px;background:rgba(20,20,20,.7);color:#fff;padding:12px 20px}
.hero-caption h1{font-size:20px;font-weight:600;margin-bottom:14px;white-space:nowrap}
.hero-caption p{font-size:12px;font-weight:600;line-height:24px;letter-spacing:-.2px;width:210px}
.read-more{left:117px;top:380px;width:88px;height:23px;background:var(--red);color:#fff;font-size:12.5px;text-align:center;line-height:23px}
.dots{left:222px;top:387px;display:flex;gap:3px}
.dots i{width:7px;height:7px;border-radius:50%;background:#fff}
.dots i.on{background:var(--navy)}
.hero-arrow{top:287px;width:48px;height:48px;border-radius:50%;background:rgba(255,255,255,.55)}

/* calls to action */
.cta{width:155px;height:142px;border:3px solid var(--navy);border-radius:5px;overflow:hidden;box-shadow:0 4px 6px rgba(0,0,0,.2)}
.cta-photo{position:absolute;inset:0}
.cta-ribbon{position:absolute;left:-22px;top:16px;width:90px;transform:rotate(-45deg);background:var(--red);color:#fff;font-size:8px;font-weight:700;text-align:center;padding:2px 0}
.cta-more{position:absolute;right:26px;bottom:0;width:50px;height:13px;background:var(--navy);color:#fff;font-size:6px;font-weight:600;text-align:center;line-height:13px;border-radius:5px 5px 0 0}

/* listings */
.listings{left:0;top:691px;width:905px;height:363px;background:var(--panel);border-top:1px solid var(--rule)}
.categories{left:95px;top:733px;width:208px;height:264px;background:var(--navy);box-shadow:0 12px 12px -6px rgba(0,0,0,.35)}
.categories h2{position:absolute;left:0;top:14px;width:100%;text-align:center;color:#fff;font-size:17px;font-weight:700;padding-bottom:9px;border-bottom:2px solid #2d3f8a}
.cat-row{position:absolute;left:26px;width:158px;height:19px;background:var(--navy-row);color:#fff;font-size:9.5px;font-weight:700;display:flex;justify-content:space-between;padding:3px 8px}
.cat-all{position:absolute;left:26px;top:226px;width:158px;height:19px;background:#e8e8e8;color:var(--navy);font-size:10px;font-weight:700;text-align:center;line-height:19px;border-radius:2px}
.section-title{left:327px;top:735px;font-size:11.5px;font-weight:700;color:var(--navy)}
.pager{top:742px;width:9px;height:10px;background:var(--navy)}
.auction{width:148px;height:111px;background:#fff;border:2px solid var(--navy);border-radius:6px;padding:6px}
.auction-photo{position:absolute;left:6px;top:6px;width:58px;height:50px;background:linear-gradient(#9fb6cf,#6d7480 60%,#8d9678)}
.auction h3{position:absolute;left:70px;top:7px;font-family:"Tinos",serif;font-weight:400;font-size:8px;color:var(--ink);white-space:nowrap}
.auction p{position:absolute;left:70px;top:20px;width:72px;font-size:5.2px;line-height:7.6px;color:var(--grey-text)}
.tags{position:absolute;left:10px;top:62px;display:flex;gap:4px}
.tags span{background:#3a4760;color:#fff;font-size:3.5px;padding:1px 4px;border-radius:2px}
.meta{position:absolute;left:6px;top:77px;font-size:3.8px;line-height:5px;color:#444}
.bid{position:absolute;left:67px;top:79px;width:67px;height:15px;background:var(--orange);color:#fff;font-size:6px;font-weight:700;text-align:center;line-height:15px;border-radius:2px}

/* footer */
.site-footer{left:0;top:1054px;width:905px;height:146px;background:var(--navy)}
.footer-text{color:var(--white)}
.footer-brand{left:98px;top:1080px;color:var(--white)}
.footer-brand .brand-mark{background:var(--white)}
.social{top:1132px;width:26px;height:26px;border-radius:3px}
.copyright{left:96px;top:1172px;font-size:8.5px;font-weight:600;white-space:nowrap}
.footer-title{font-size:14.5px;font-weight:400;top:1074px}
.quick-links{left:295px;top:1104px;display:grid;grid-template-columns:71px auto;row-gap:6px;font-size:9.5px;line-height:13px;list-style:none}
.post{top:1098px;width:158px;font-size:8px;line-height:14.5px}
.post h4{font-size:9px;font-weight:700;margin-bottom:3px;display:flex;align-items:center;gap:6px;white-space:nowrap}
.chev{color:var(--red);font-weight:700;letter-spacing:-2px}
</style>
</head>
<body>

<header class="site-header abs"></header>
<div class="brand header-brand abs"><span class="brand-mark"></span>BREVIN AUCTIONS</div>
<div class="contact-line abs">(555) 014-2290<span>info@brevin.example</span></div>
<div class="search abs">Search Website</div>
<div class="search-btn abs">
  <svg width="20" height="19" viewBox="0 0 20 19"><circle cx="9" cy="8.5" r="3.5" fill="none" stroke="#fff" stroke-width="1.6"/><line x1="11.5" y1="11" x2="14.5" y2="14" stroke="#fff" stroke-width="1.8"/></svg>
</div>
<div class="lang abs"><span class="flag" role="img" aria-label="English flag"></span>EN
  <svg width="12" height="8" viewBox="0 0 12 8"><path d="M0 0h12L6 8z" fill="#444"/></svg>
</div>

<nav class="main-nav abs">
  <ul>
    <li>Home</li><li>Auctions</li><li class="current">Services</li><li>Real Estate</li><li>Previous Auctions</li><li>About Us</li><li>Contact Us</li>
  </ul>
</nav>

<section class="hero abs" role="img" aria-label="Auctioneer on stage presenting a quilt to a seated crowd"></section>
<div class="hero-caption abs">
  <h1>Lorem Ipsum Dolor</h1>
  <p>Lorem ipsum dolor sit amet, consectetur adipisicing elit, sed do eiusmod tempor incididunt ut</p>
</div>
<div class="read-more abs">Read More</div>
<div class="dots abs"><i></i><i class="on"></i><i></i><i></i></div>
<div class="hero-arrow abs" style="left:45px">
  <svg width="48" height="48" viewBox="0 0 48 48"><path d="M28 12 16 24l12 12M16 24h18" fill="none" stroke="#555" stroke-width="6"/></svg>
</div>
<div class="hero-arrow abs" style="left:806px">
  <svg width="48" height="48" viewBox="0 0 48 48"><path d="M20 12l12 12-12 12M32 24H14" fill="none" stroke="#333" stroke-width="6"/></svg>
</div>
<div class="dropdown abs"><div>Lorem Ipsum</div><div>Lorem Ipsum</div></div>

<div class="cta abs" style="left:113px;top:505px">
  <div class="cta-photo" role="img" aria-label="Two-storey suburban house under blue sky" style="background:linear-gradient(#3b6fd0,#8fb2e6 45%,#b7b3aa 70%,#5d6b4a)"></div>
  <div class="cta-ribbon">Real Estate</div><div class="cta-more">Read More</div>
</div>
<div class="cta abs" style="left:288px;top:505px">
  <div class="cta-photo" role="img" aria-label="Bidder raising a numbered paddle at an auction" style="background:linear-gradient(135deg,#7d6a55,#3e3a37 60%,#b9b2a6)"></div>
  <div class="cta-ribbon">Auctions</div><div class="cta-more">Read More</div>
</div>
<div class="cta abs" style="left:463px;top:505px">
  <div class="cta-photo" role="img" aria-label="Store with red liquidation sale signs" style="background:linear-gradient(#c9cbd1,#d8322e 40%,#c33 60%,#8a93a8)"></div>
  <div class="cta-ribbon">Liquidation</div><div class="cta-more">Read More</div>
</div>
<div class="cta abs" style="left:637px;top:505px">
  <div class="cta-photo" role="img" aria-label="Real estate appraisal document with a pen" style="background:linear-gradient(160deg,#111 30%,#e8e8e8 45%,#fafafa 80%,#222)"></div>
  <div class="cta-ribbon">Appraisals</div><div class="cta-more">Read More</div>
</div>

<section class="listings abs"></section>
<aside class="categories abs">
  <h2>CATEGORIES</h2>
  <div class="cat-row" style="top:60px"><span>Real Estate</span><span>12</span></div>
  <div class="cat-row" style="top:91px"><span>Auctions</span><span>12</span></div>
  <div class="cat-row" style="top:121px"><span>Lorem Ipsum</span><span>12</span></div>
  <div class="cat-row" style="top:152px"><span>Lorem Ipsum</span><span>12</span></div>
  <div class="cat-row" style="top:182px"><span>Lorem Ipsum</span><span>12</span></div>
  <div class="cat-all">SHOW ALL CATEGORIES</div>
</aside>

<h2 class="section-title abs">CURRENT AUCTIONS</h2>
<div class="pager abs" style="left:786px"><svg width="9" height="10"><path d="M6 2 3 5l3 3" fill="none" stroke="#fff" stroke-width="1.3"/></svg></div>
<div class="pager abs" style="left:797px"><svg width="9" height="10"><path d="M3 2l3 3-3 3" fill="none" stroke="#fff" stroke-width="1.3"/></svg></div>

<article class="auction abs" style="left:324px;top:762px">
  <div class="auction-photo" role="img" aria-label="House for auction"></div>
  <h3>Pellentesque acsan</h3>
  <p>Lorem ipsum is a dummy text only. Dolor sit amet, consectetur adipiscing elit. Nullam felis mauris, eleifend ac rhoncus non, lobortis at diam rurna.</p>
  <div class="tags"><span>Online</span><span>Estate</span></div>
  <div class="meta">Online bidding<br>Begins: 07/24 6:00 PM<br>Ends: 08/01 6:00 PM</div>
  <div class="bid">Click to bid online</div>
</article>
<article class="auction abs" style="left:491px;top:762px">
  <div class="auction-photo" role="img" aria-label="House for auction"></div>
  <h3>Pellentesque acsan</h3>
  <p>Lorem ipsum is a dummy text only. Dolor sit amet, consectetur adipiscing elit. Nullam felis mauris, eleifend ac rhoncus non, lobortis at diam rurna.</p>
  <div class="tags"><span>Online</span><span>Estate</span></div>
  <div class="meta">Online bidding<br>Begins: 07/24 6:00 PM<br>Ends: 08/01 6:00 PM</div>
  <div class="bid">Click to bid online</div>
</article>
<article class="auction abs" style="left:657px;top:762px">
  <div class="auction-photo" role="img" aria-label="House for auction"></div>
  <h3>Pellentesque acsan</h3>
  <p>Lorem ipsum is a dummy text only. Dolor sit amet, consectetur adipiscing elit. Nullam felis mauris, eleifend ac rhoncus non, lobortis at diam rurna.</p>
  <div class="tags"><span>Online</span><span>Estate</span></div>
  <div class="meta">Online bidding<br>Begins: 07/24 6:00 PM<br>Ends: 08/01 6:00 PM</div>
  <div class="bid">Click to bid online</div>
</article>
<article class="auction abs" style="left:324px;top:886px">
  <div class="auction-photo" role="img" aria-label="House for auction"></div>
  <h3>Pellentesque acsan</h3>
  <p>Lorem ipsum is a dummy text only. Dolor sit amet, consectetur adipiscing elit. Nullam felis mauris, eleifend ac rhoncus non, lobortis at diam rurna.</p>
  <div class="tags"><span>Online</span><span>Estate</span></div>
  <div class="meta">Online bidding<br>Begins: 07/24 6:00 PM<br>Ends: 08/01 6:00 PM</div>
  <div class="bid">Click to bid online</div>
</article>
<article class="auction abs" style="left:491px;top:886px">
  <div class="auction-photo" role="img" aria-label="House for auction"></div>
  <h3>Pellentesque acsan</h3>
  <p>Lorem ipsum is a dummy text only. Dolor sit amet, consectetur adipiscing elit. Nullam felis mauris, eleifend ac rhoncus non, lobortis at diam rurna.</p>
  <div class="tags"><span>Online</span><span>Estate</span></div>
  <div class="meta">Online bidding<br>Begins: 07/24 6:00 PM<br>Ends: 08/01 6:00 PM</div>
  <div class="bid">Click to bid online</div>
</article>
<article class="auction abs" style="left:657px;top:886px">
  <div class="auction-photo" role="img" aria-label="House for auction"></div>
  <h3>Pellentesque acsan</h3>
  <p>Lorem ipsum is a dummy text only. Dolor sit amet, consectetur adipiscing elit. Nullam felis mauris, eleifend ac rhoncus non, lobortis at diam rurna.</p>
  <div class="tags"><span>Online</span><span>Estate</span></div>
  <div class="meta">Online bidding<br>Begins: 07/24 6:00 PM<br>Ends: 08/01 6:00 PM</div>
  <div class="bid">Click to bid online</div>
</article>

<footer class="site-footer abs"></footer>
<div class="brand footer-brand abs"><span class="brand-mark"></span>BREVIN AUCTIONS</div>
<div class="social abs" style="left:98px;background:#c4161c" role="img" aria-label="Video channel link"></div>
<div class="social abs" style="left:141px;background:#3b5998" role="img" aria-label="Social page link"></div>
<div class="social abs" style="left:184px;background:#f26522" role="img" aria-label="News feed link"></div>
<div class="social abs" style="left:226px;background:#1da1f2" role="img" aria-label="Short posts link"></div>
<div class="copyright footer-text abs">Copyright©Brevin2014. All Rights Reserved</div>

<h3 class="footer-title footer-text abs" style="left:295px">Quick Links</h3>
<ul class="quick-links footer-text abs">
  <li>Home</li><li>Previous Auctions</li>
  <li>Auctions</li><li>About Us</li>
  <li>Services</li><li>Contact Us</li>
  <li>Real Estate</li>
</ul>

<h3 class="footer-title footer-text abs" style="left:497px">Older Posts</h3>
<div class="post footer-text abs" style="left:501px">
  <h4><span class="chev">››</span>Lorem Ipsum Dolorum</h4>
  Lorem ipsum is a dummy text only. Dolor sit amet, consectetur adipiscing elit. Nullam felis mauris... [Read more]
</div>
<div class="post footer-text abs" style="left:670px">
  <h4><span class="chev">››</span>Lorem Ipsum Dolorum</h4>
  Lorem ipsum is a dummy text only. Dolor sit amet, consectetur adipiscing elit. Nullam felis mauris... [Read more]
</div>

</body>
</html>
```